Tech business card design

We need an amazing business card design for our new business 'Brakka' a marketing tech startup based in Sydney, Australia. We provide an online marketplace for businesses to search and buy advertising media, connect with service providers and learn more about marketing. We wish to communicate 'cool tech', reliability and professionalism and design based around our logo.

Target Market(s)

Business Owners

Contact Information for Business Card

Name
Position
Email Address
Website
Phone Number

Font styles to use
Other font styles liked:
• Avenir & Avenir Next

Colors

Designer to choose colors to be used in the design.

```html
<!DOCTYPE html>
<html lang="en">
<head>
<meta charset="utf-8">
<title>Brakka — Business Card</title>
<link href="https://fonts.googleapis.com/css2?family=Titillium+Web:wght@400;700;900&display=swap" rel="stylesheet">
<style>
  :root {
    --stage: #ebebeb;
    --paper: #f3f3f1;
    --navy: #221f4f;
    --pattern-light: #dcdcdf;
    --pattern-mid: #8a86a3;
    --white: #ffffff;
  }
  * { margin: 0; padding: 0; box-sizing: border-box; }
  html, body {
    width: 1200px;
    height: 800px;
    overflow: hidden;
    background: var(--stage);
    font-family: "Titillium Web", sans-serif;
  }
  .stage {
    position: relative;
    width: 1200px;
    height: 800px;
  }
  .card {
    position: absolute;
    top: 280px;
    width: 418px;
    height: 240px;
    background: var(--paper);
    overflow: hidden;
    box-shadow: 0 1px 2px rgba(0,0,0,0.08);
  }
  .card--front { left: 143px; }
  .card--back { left: 639px; }

  .pattern {
    position: absolute;
    top: 0;
    height: 100%;
    background: linear-gradient(160deg, var(--pattern-light) 0%, var(--pattern-mid) 45%, var(--pattern-light) 70%, var(--pattern-mid) 100%);
    opacity: 0.55;
  }
  .card--front .pattern { left: 247px; width: 171px; }
  .card--back .pattern { left: 0; width: 171px; }

  .brand-name {
    position: absolute;
    left: 26px;
    top: 146px;
    font-size: 48px;
    font-weight: 900;
    line-height: 1;
    letter-spacing: -0.5px;
    color: var(--navy);
  }

  .contact-panel {
    position: absolute;
    left: 171px;
    top: 0;
    width: 247px;
    height: 100%;
    background: var(--navy);
    color: var(--white);
    text-align: right;
    padding: 54px 42px 0 0;
  }
  .contact-name {
    font-size: 19px;
    font-weight: 700;
    line-height: 1.05;
  }
  .contact-role {
    font-size: 16px;
    font-weight: 400;
    line-height: 1.1;
  }
  .contact-details {
    list-style: none;
    margin-top: 32px;
    font-size: 17px;
    font-weight: 400;
    line-height: 1.18;
  }
</style>
</head>
<body>
  <main class="stage">
    <section class="card card--front">
      <div class="brand-name">Brakka</div>
      <div class="pattern" role="img" aria-label="Geometric pattern of navy, violet and grey triangles"></div>
    </section>

    <section class="card card--back">
      <div class="pattern" role="img" aria-label="Geometric pattern of navy, violet and grey triangles"></div>
      <div class="contact-panel">
        <p class="contact-name">Owen Ferris</p>
        <p class="contact-role">manager</p>
        <ul class="contact-details">
          <li>012 345 6789</li>
          <li>your@email.com</li>
          <li>www.website.com</li>
        </ul>
      </div>
    </section>
  </main>
</body>
</html>
```